Service Menu refresh 2018 Update of menu pricing

We currently have service menus as attached. We will be updating our look via our homepage image, our service menu and our in-house beverage and treatment menu.
We are a natural and sustainable hair salon group and moving more towards head spa which consists of treatments, beauty, tanning as well as your traditional hair services. Our imagery needs to reflect our efforts in spa treatments in the hair and scalp area and use natural materials and colours reflecting sustainability.
Elvu is the brand we stock and promote.

Target Market(s)

Men or women interesting in personal maintenance with natural and organic products and using sustainable practises

Industry/Entity Type

Hair And Beauty

Font styles to use
Sans Serif
Other font styles liked:
• Arial or Helvetica

Colors
9acb3c
abd037
cadf82
ffffff

Requirements
Must have
• Name on the front cover, locations on back cover
Nice to have
• Prestige feel, reflect male and female clients
Should not have
• Bold artificial writing or any type of cartoon images.
• Same images as existing menu.

```html
<!DOCTYPE html>
<html lang="en">
<head>
<meta charset="utf-8">
<title>purelyverdant hair studios — Service Menu</title>
<link href="https://fonts.googleapis.com/css2?family=Lilita+One&family=Source+Sans+3:wght@400;600;700&family=Oswald:wght@500&display=swap" rel="stylesheet">
<style>
  :root{
    --bg:#e6e7e8;
    --white:#ffffff;
    --green:#6fbe3d;
    --green-bright:#9acb3c;
    --green-light:#cadf82;
    --green-pale:#cfe9b4;
    --ink:#1d3411;
    --ink-soft:#222;
    --head:#111;
  }
  *{box-sizing:border-box;margin:0;padding:0}
  html,body{width:1200px;height:1200px;overflow:hidden;background:var(--bg)}
  body{position:relative;font-family:"Source Sans 3",Arial,sans-serif}

  .card{position:absolute;left:205px;width:790px;height:563px;overflow:hidden;box-shadow:0 6px 14px rgba(0,0,0,.35)}
  .card--front{top:30px}
  .card--back{top:607px;background:var(--white)}

  /* front cover */
  .cover-photo{position:absolute;inset:0;
    background:radial-gradient(ellipse at 55% 45%,#8a6b52 0%,#4a3a2c 25%,transparent 50%),
               linear-gradient(120deg,#3b3f34 0%,#5b6452 35%,#2c3a24 65%,#1e2a18 100%)}
  .cover-foliage{position:absolute;right:0;top:0;width:270px;height:563px;
    background:linear-gradient(160deg,#9fd08a 0%,#5aa65a 40%,#2e6b34 100%);
    clip-path:polygon(40% 0,100% 0,100% 100%,12% 100%,30% 70%,0 42%,28% 25%)}
  .cover-frame{position:absolute;inset:10px;border:1px solid rgba(255,255,255,.6)}
  .cover-brand{position:absolute;left:202px;top:76px;color:var(--white);font-weight:600;font-size:34px;letter-spacing:.3px;display:flex;align-items:center;gap:12px}
  .cover-brand .dot{width:18px;height:18px;border-radius:50%;background:var(--green-bright)}
  .cover-url{position:absolute;left:37px;top:521px;color:var(--white);font-size:14px}

  /* back cover */
  .edge-right{position:absolute;right:0;top:0;width:7px;height:100%;background:var(--green)}
  .edge-bottom{position:absolute;left:150px;bottom:0;width:100%;height:6px;background:var(--green)}
  .back-foliage{position:absolute;left:0;top:0;width:200px;height:563px;
    background:linear-gradient(170deg,#b7c77a 0%,#5f8f4a 35%,#2f5c33 70%,#1f3d22 100%);
    clip-path:polygon(0 0,50% 0,35% 14%,28% 40%,22% 55%,45% 62%,20% 75%,75% 100%,0 100%)}
  .back-brand{position:absolute;left:540px;top:36px;font-weight:600;font-size:21px;color:var(--ink-soft);display:flex;align-items:center;gap:10px}
  .back-brand .dot{width:26px;height:26px;border-radius:50%;background:var(--green)}
  .panel-rule{position:absolute;left:440px;top:95px;width:343px;height:1px;background:#eee}

  .heading{position:absolute;font-family:"Lilita One",Arial,sans-serif;color:var(--ink);letter-spacing:.5px;line-height:1}
  .heading--xl{font-size:25px}
  .heading--md{font-size:16px}
  .item{position:absolute;font-size:11px;color:var(--ink-soft);line-height:1}
  .item--strong{font-weight:700}
  .note{position:absolute;left:447px;font-size:7.5px;color:var(--ink-soft)}

  .col-head{position:absolute;width:34px;height:28px;background:var(--head);color:var(--white);
    font-family:"Lilita One",Arial,sans-serif;font-size:13px;display:flex;align-items:center;justify-content:center;
    border-bottom:3px solid var(--green)}
  .bar{position:absolute;width:34px}
  .bar--dark{background:var(--green)}
  .bar--light{background:var(--green-pale)}

  .price-row{position:absolute;left:0;width:100%;height:12px}
  .price{position:absolute;font-family:"Oswald",Arial,sans-serif;font-size:10px;color:var(--ink);line-height:1}
  .price sup{font-size:6px}
  .table-cut .s{left:266px}.table-cut .m{left:306px}.table-cut .l{left:347px}.table-cut .xl{left:388px}
  .table-colour .s{left:612px}.table-colour .m{left:652px}.table-colour .l{left:694px}.table-colour .xl{left:734px}
</style>
</head>
<body>

<section class="card card--front">
  <div class="cover-photo" role="img" aria-label="Photo of a woman in a wide-brim hat and sunglasses among greenhouse plants"></div>
  <div class="cover-foliage" role="img" aria-label="Illustrated tropical leaves and ferns"></div>
  <div class="cover-frame"></div>
  <div class="cover-brand"><span class="dot"></span>purelyverdant hair studios</div>
  <div class="cover-url">www.verdanthairstudios.com.au</div>
</section>

<section class="card card--back">
  <div class="back-foliage" role="img" aria-label="Illustrated ferns and tropical leaves"></div>
  <div class="edge-right"></div>
  <div class="edge-bottom"></div>
  <div class="back-brand"><span class="dot"></span>purelyverdant hair studios</div>
  <div class="panel-rule"></div>

  <!-- cut & blowdry table -->
  <div class="table-cut">
    <div class="heading heading--xl" style="left:133px;top:76px;line-height:1.05">CUT &amp;<br>BLOWDRY</div>
    <div class="col-head" style="left:262px;top:96px">S</div>
    <div class="col-head" style="left:302px;top:96px">M</div>
    <div class="col-head" style="left:343px;top:96px">L</div>
    <div class="col-head" style="left:384px;top:96px">XL</div>
    <div class="bar bar--dark" style="left:262px;top:128px;height:395px"></div>
    <div class="bar bar--light" style="left:302px;top:128px;height:395px"></div>
    <div class="bar bar--dark" style="left:343px;top:128px;height:395px"></div>
    <div class="bar bar--light" style="left:384px;top:128px;height:395px"></div>

    <div class="heading heading--md" style="left:133px;top:144px">LADIES FRINGE</div>
    <div class="item" style="left:133px;top:169px">Trim</div>
    <div class="item" style="left:133px;top:182px">Restyle</div>
    <div class="heading heading--md" style="left:133px;top:209px">MENS</div>
    <div class="item" style="left:133px;top:229px">Single clipper</div>
    <div class="item" style="left:133px;top:243px">Style cut</div>
    <div class="heading heading--md" style="left:133px;top:263px">CHILDREN</div>
    <div class="item" style="left:133px;top:289px">10 and under</div>
    <div class="item" style="left:133px;top:306px">11-16 male</div>
    <div class="item" style="left:133px;top:322px">11-16 female</div>
    <div class="item" style="left:133px;top:339px">add a wash</div>
    <div class="heading heading--md" style="left:133px;top:360px">BLOWDRY</div>
    <div class="item" style="left:133px;top:383px">Shampoo &amp; dry off</div>
    <div class="heading heading--md" style="left:133px;top:404px">TREATMENTS</div>
    <div class="item" style="left:133px;top:429px">Deep treatment</div>
    <div class="item" style="left:133px;top:444px">Head spa ritual</div>
    <div class="heading heading--md" style="left:133px;top:462px">UPSTYLE</div>
    <div class="item" style="left:133px;top:487px">45 minutes</div>
    <div class="item" style="left:133px;top:502px">60 minutes</div>

    <div class="price-row" style="top:149px"><span class="price s"><sup>$</sup>77</span><span class="price m"><sup>$</sup>88</span><span class="price l"><sup>$</sup>99</span><span class="price xl"><sup>$</sup>110</span></div>
    <div class="price-row" style="top:170px"><span class="price s"><sup>$</sup>25</span></div>
    <div class="price-row" style="top:183px"><span class="price s"><sup>$</sup>35</span></div>
    <div class="price-row" style="top:230px"><span class="price s"><sup>$</sup>28</span></div>
    <div class="price-row" style="top:244px"><span class="price s"><sup>$</sup>42</span></div>
    <div class="price-row" style="top:288px"><span class="price s"><sup>$</sup>24</span></div>
    <div class="price-row" style="top:309px"><span class="price s"><sup>$</sup>32</span></div>
    <div class="price-row" style="top:329px"><span class="price s"><sup>$</sup>48</span></div>
    <div class="price-row" style="top:349px"><span class="price s"><sup>$</sup>5</span><span class="price m"><sup>$</sup>57</span><span class="price l"><sup>$</sup>67</span><span class="price xl"><sup>$</sup>77</span></div>
    <div class="price-row" style="top:370px"><span class="price s"><sup>$</sup>47</span></div>
    <div class="price-row" style="top:390px"><span class="price s"><sup>$</sup>25</span></div>
    <div class="price-row" style="top:433px"><span class="price s"><sup>$</sup>35</span></div>
    <div class="price-row" style="top:447px"><span class="price s"><sup>$</sup>65</span></div>
    <div class="price-row" style="top:486px"><span class="price s"><sup>$</sup>85</span></div>
    <div class="price-row" style="top:499px"><span class="price s"><sup>$</sup>120</span></div>
  </div>

  <!-- colour table -->
  <div class="table-colour">
    <div class="col-head" style="left:608px;top:127px">S</div>
    <div class="col-head" style="left:648px;top:127px">M</div>
    <div class="col-head" style="left:690px;top:127px">L</div>
    <div class="col-head" style="left:730px;top:127px">XL</div>
    <div class="bar bar--dark" style="left:608px;top:160px;height:367px"></div>
    <div class="bar bar--light" style="left:648px;top:160px;height:367px"></div>
    <div class="bar bar--dark" style="left:690px;top:160px;height:367px"></div>
    <div class="bar bar--light" style="left:730px;top:160px;height:367px"></div>

    <div class="heading heading--xl" style="left:447px;top:135px;font-size:23px">COLOUR</div>
    <div class="item" style="left:448px;top:172px">Regrowth</div>
    <div class="item" style="left:448px;top:188px">FULL colour tint</div>
    <div class="item" style="left:448px;top:205px">ROOTGLOW lightening</div>
    <div class="item" style="left:448px;top:222px">BALAYAGE/OMBRE</div>
    <div class="heading heading--md" style="left:448px;top:252px">BLOOMTINT</div>
    <div class="item" style="left:448px;top:282px">Regrowth</div>
    <div class="item" style="left:448px;top:308px">FULL colour tint</div>
    <div class="heading heading--xl" style="left:447px;top:337px;font-size:23px">FOILS</div>
    <div class="item" style="left:448px;top:375px">Single</div>
    <div class="item" style="left:448px;top:390px">1/4 head</div>
    <div class="item" style="left:448px;top:405px">1/2 head</div>
    <div class="item" style="left:448px;top:420px">Full head</div>
    <div class="heading heading--xl" style="left:447px;top:441px;font-size:23px">STRAIGHT</div>
    <div class="item item--strong" style="left:447px;top:472px">SILKEN 5mm SYSTEM</div>
    <div class="note" style="top:494px">• Includes colour match &amp; toner</div>
    <div class="note" style="top:504px">• Minimum 6 foils without colour</div>
    <div class="note" style="top:514px">• Minimum charge on a Sunday is $40</div>

    <div class="price-row" style="top:172px"><span class="price s"><sup>$</sup>83</span></div>
    <div class="price-row" style="top:188px"><span class="price s"><sup>$</sup>125</span><span class="price m"><sup>$</sup>165</span><span class="price l"><sup>$</sup>145</span><span class="price xl"><sup>$</sup>185</span></div>
    <div class="price-row" style="top:205px"><span class="price s"><sup>$</sup>165</span><span class="price m"><sup>$</sup>209</span><span class="price l"><sup>$</sup>189</span><span class="price xl"><sup>$</sup>229</span></div>
    <div class="price-row" style="top:222px"><span class="price m"><sup>$</sup>375</span><span class="price l"><sup>$</sup>275</span><span class="price xl"><sup>$</sup>475</span></div>
    <div class="price-row" style="top:288px"><span class="price s"><sup>$</sup>99</span></div>
    <div class="price-row" style="top:297px"><span class="price m"><sup>$</sup>175</span><span class="price l"><sup>$</sup>195</span><span class="price xl"><sup>$</sup>205</span></div>
    <div class="price-row" style="top:301px"><span class="price s"><sup>$</sup>155</span></div>
    <div class="price-row" style="top:374px"><span class="price s"><sup>$</sup>11</span><span class="price m"><sup>$</sup>13</span><span class="price l"><sup>$</sup>17</span><span class="price xl"><sup>$</sup>22</span></div>
    <div class="price-row" style="top:387px"><span class="price s"><sup>$</sup>135</span><span class="price m"><sup>$</sup>155</span><span class="price l"><sup>$</sup>175</span><span class="price xl"><sup>$</sup>195</span></div>
    <div class="price-row" style="top:400px"><span class="price s"><sup>$</sup>185</span><span class="price m"><sup>$</sup>205</span><span class="price l"><sup>$</sup>235</span><span class="price xl"><sup>$</sup>265</span></div>
    <div class="price-row" style="top:413px"><span class="price s"><sup>$</sup>235</span><span class="price m"><sup>$</sup>265</span><span class="price l"><sup>$</sup>315</span><span class="price xl"><sup>$</sup>355</span></div>
    <div class="price-row" style="top:467px"><span class="price s"><sup>$</sup>365</span><span class="price m"><sup>$</sup>445</span><span class="price l"><sup>$</sup>535</span><span class="price xl"><sup>$</sup>565</span></div>
  </div>
</section>

</body>
</html>
```